Tasteful instructions for employees/guests to wash hands

Need an aesthetic visualisation of steps to wash hands.
While we would like to convey the proper steps to wash hands we also don't want to treat our staff/guests like children, rather provide a quick reminder.
Suggested sizes
16″ × 24″
11″ × 14″
A simplified version of these steps:
- Wet your hands with clean, running water (warm or cold), turn off the tap, and apply soap.
- Lather your hands by rubbing them together with the soap. Lather the backs of your hands, between your fingers, and under your nails.
- Scrub your hands for at least 20 seconds.
- Rinse your hands well under clean, running water.
- Dry your hands using a clean towel or air dry them.
Look and feel
Each slider illustrates characteristics of the customer's brand and the style your logo design should communicate.

```html
<!DOCTYPE html>
<html lang="en">
<head>
<meta charset="utf-8">
<title>How To Hand Wash</title>
<link rel="stylesheet" href="https://fonts.googleapis.com/css2?family=Barlow:wght@400;500;600&display=swap">
<style>
  :root {
    --canvas-bg: #f4f5f7;
    --paper: #dde3ea;
    --sky-light: #2f93d8;
    --sky-deep: #0d3684;
    --ring: #8db3e4;
    --panel: #9dbfe9;
    --navy: #1b3d8e;
    --badge: #13337a;
    --white: #ffffff;
    --skin: #f6a26b;
    --skin-soft: #fbd2b0;
    --water: #4c8fd6;
  }
  * { margin: 0; padding: 0; box-sizing: border-box; }
  html, body {
    width: 1200px; height: 581px; overflow: hidden;
    background: var(--canvas-bg);
  }
  .stage {
    position: relative; width: 1200px; height: 581px;
    display: flex; align-items: center; justify-content: center;
  }
  .poster {
    width: 426px; height: 543px; display: block;
    box-shadow: 0 4px 14px rgba(20, 40, 80, 0.12);
  }
  .poster text { font-family: "Barlow", sans-serif; }
  .title { fill: var(--white); font-weight: 500; text-anchor: middle; letter-spacing: 1px; }
  .step-label { fill: var(--navy); font-size: 20px; font-weight: 500; text-anchor: middle; }
  .step-note { fill: var(--navy); font-size: 14px; font-weight: 500; text-anchor: middle; letter-spacing: 0.5px; }
  .badge-num { fill: var(--white); font-size: 17px; font-weight: 600; text-anchor: middle; }
  .timer-text { fill: var(--navy); font-size: 18px; font-weight: 500; text-anchor: middle; }
  .timer-strong { font-weight: 600; }
</style>
</head>
<body>
<main class="stage">
  <svg class="poster" viewBox="0 0 857 1092" xmlns="http://www.w3.org/2000/svg" aria-labelledby="poster-title">
    <title id="poster-title">How to hand wash – eight steps</title>
    <defs>
      <linearGradient id="sky" x1="0" y1="0" x2="1" y2="0.4">
        <stop offset="0" stop-color="var(--sky-light)"/>
        <stop offset="1" stop-color="var(--sky-deep)"/>
      </linearGradient>
      <linearGradient id="scene-wash" x1="0" y1="0" x2="0" y2="1">
        <stop offset="0" stop-color="#ffffff"/>
        <stop offset="0.3" stop-color="#dfeaf8"/>
        <stop offset="0.5" stop-color="var(--skin-soft)"/>
        <stop offset="1" stop-color="var(--skin)"/>
      </linearGradient>
      <linearGradient id="scene-hands" x1="0" y1="0" x2="1" y2="1">
        <stop offset="0" stop-color="#ffffff"/>
        <stop offset="0.45" stop-color="var(--skin-soft)"/>
        <stop offset="1" stop-color="var(--skin)"/>
      </linearGradient>
    </defs>

    <rect class="paper" width="857" height="1092" fill="var(--paper)"/>

    <path class="header-band" fill="url(#sky)"
      d="M0 0 H857 V165 Q830 170 815 200 Q790 195 780 222 Q745 215 735 245 Q700 236 688 262 Q652 255 640 285 Q602 280 585 300 Q548 290 522 302 Q490 290 470 300 Q440 286 410 300 Q380 286 350 294 Q322 280 300 264 Q272 254 252 240 Q222 230 200 226 Q172 214 150 230 Q122 220 100 226 Q72 214 50 230 Q25 220 0 232 Z"/>
    <g class="droplets" fill="var(--white)" opacity="0.85">
      <circle cx="112" cy="195" r="10"/>
      <circle cx="730" cy="170" r="8"/>
      <circle cx="598" cy="253" r="11"/>
    </g>
    <g class="droplets-faint" fill="none" stroke="#6fb0e8" stroke-width="3" opacity="0.6">
      <circle cx="45" cy="22" r="9"/><circle cx="100" cy="140" r="8"/>
      <circle cx="780" cy="25" r="10"/><circle cx="830" cy="60" r="7"/>
      <circle cx="225" cy="100" r="8"/>
    </g>
    <text class="title" x="428" y="120" font-size="52">HOW TO</text>
    <text class="title" x="428" y="196" font-size="72">HAND WASH</text>

    <g class="step">
      <circle cx="204" cy="397" r="84" fill="url(#scene-wash)" role="img" aria-label="Illustration: two open hands under falling water drops"/>
      <circle cx="204" cy="397" r="85" fill="none" stroke="var(--ring)" stroke-width="17"/>
      <circle cx="126" cy="339" r="17" fill="var(--badge)"/><text class="badge-num" x="126" y="345">1</text>
      <text class="step-label" x="204" y="515">Wet Hands</text>
    </g>
    <g class="step">
      <circle cx="430" cy="397" r="84" fill="url(#scene-hands)" role="img" aria-label="Illustration: a hand turning off a tap, water stopped"/>
      <circle cx="430" cy="397" r="85" fill="none" stroke="var(--ring)" stroke-width="17"/>
      <circle cx="352" cy="339" r="17" fill="var(--badge)"/><text class="badge-num" x="352" y="345">2</text>
      <text class="step-label" x="430" y="515">Off Tap</text>
    </g>
    <g class="step">
      <circle cx="655" cy="397" r="84" fill="url(#scene-wash)" role="img" aria-label="Illustration: a soap dispenser pumping soap into an open hand"/>
      <circle cx="655" cy="397" r="85" fill="none" stroke="var(--ring)" stroke-width="17"/>
      <circle cx="577" cy="339" r="17" fill="var(--badge)"/><text class="badge-num" x="577" y="345">3</text>
      <text class="step-label" x="655" y="515">Apply Soap</text>
    </g>

    <g class="scrub-group">
      <path d="M60 541 H150 V817 H60 A22 22 0 0 1 38 795 V563 A22 22 0 0 1 60 541 Z" fill="var(--panel)"/>
      <rect x="38" y="541" width="786" height="276" rx="22" fill="none" stroke="var(--ring)" stroke-width="5"/>
      <g class="timer-icon" stroke="var(--badge)" fill="none" stroke-width="4" stroke-linecap="round">
        <path d="M70 652 A38 38 0 1 1 95 665"/>
        <path d="M62 643 L68 655 L80 649"/>
        <path d="M95 589 V596 M133 627 H126 M122 600 L117 605"/>
      </g>
      <text class="timer-text" x="95" y="632" font-size="25" font-weight="600">20</text>
      <text class="timer-text" x="95" y="646" font-size="12" font-weight="600">SEC</text>
      <text class="timer-text" x="93" y="694">Scub Your</text>
      <text class="timer-text" x="93" y="714">Hands For</text>
      <text class="timer-text" x="93" y="733">At Least</text>
      <text class="timer-text timer-strong" x="93" y="753">20 Seconds</text>
    </g>

    <g class="step">
      <circle cx="259" cy="647" r="84" fill="url(#scene-hands)" role="img" aria-label="Illustration: soapy palms rubbing together in a circular motion"/>
      <circle cx="259" cy="647" r="85" fill="none" stroke="var(--ring)" stroke-width="17"/>
      <circle cx="181" cy="589" r="17" fill="var(--badge)"/><text class="badge-num" x="181" y="595">4</text>
      <text class="step-label" x="259" y="764">Rub Palms</text>
    </g>
    <g class="step">
      <circle cx="485" cy="647" r="84" fill="url(#scene-hands)" role="img" aria-label="Illustration: one palm rubbing the back of the other hand with fingers interlaced"/>
      <circle cx="485" cy="647" r="85" fill="none" stroke="var(--ring)" stroke-width="17"/>
      <circle cx="407" cy="589" r="17" fill="var(--badge)"/><text class="badge-num" x="407" y="595">5</text>
      <text class="step-label" x="485" y="764">Rub Back of Hands &amp;</text>
      <text class="step-label" x="485" y="784">Between Fingers</text>
      <text class="step-note" x="485" y="803">(repeat for other hand)</text>
    </g>
    <g class="step">
      <circle cx="710" cy="647" r="84" fill="url(#scene-hands)" role="img" aria-label="Illustration: fingertips scrubbing under the nails in the opposite palm"/>
      <circle cx="710" cy="647" r="85" fill="none" stroke="var(--ring)" stroke-width="17"/>
      <circle cx="632" cy="589" r="17" fill="var(--badge)"/><text class="badge-num" x="632" y="595">6</text>
      <text class="step-label" x="717" y="764">Wash Your Nails</text>
      <text class="step-note" x="717" y="784">(repeat for other hand)</text>
    </g>

    <g class="step">
      <circle cx="310" cy="929" r="84" fill="url(#scene-wash)" role="img" aria-label="Illustration: two open hands rinsed under falling water drops"/>
      <circle cx="310" cy="929" r="85" fill="none" stroke="var(--ring)" stroke-width="17"/>
      <circle cx="232" cy="871" r="17" fill="var(--badge)"/><text class="badge-num" x="232" y="877">7</text>
      <text class="step-label" x="310" y="1048">Rinse Hands</text>
    </g>
    <g class="step">
      <circle cx="535" cy="929" r="84" fill="url(#scene-hands)" role="img" aria-label="Illustration: hands being dried with a paper towel"/>
      <circle cx="535" cy="929" r="85" fill="none" stroke="var(--ring)" stroke-width="17"/>
      <circle cx="457" cy="871" r="17" fill="var(--badge)"/><text class="badge-num" x="457" y="877">8</text>
      <text class="step-label" x="535" y="1048">Dry Your Hands</text>
    </g>

    <g class="droplets-faint" fill="none" stroke="#9aaac4" stroke-width="3" opacity="0.7">
      <circle cx="728" cy="950" r="13"/><circle cx="745" cy="978" r="7"/>
      <circle cx="730" cy="1118" r="15"/><circle cx="798" cy="1130" r="12"/>
      <circle cx="795" cy="1080" r="6"/><circle cx="815" cy="1030" r="5"/>
    </g>
  </svg>
</main>
</body>
</html>
```